Wordpress design for my private practice website - Psychotherapist

I would like a simple, clean, and elegant design for my private practice website. I work with both adults and children so I'd like it to appeal to both. However, since parents make the choice as to where to send their child for therapy, I want it to appeal to adults more. I would like the pictures on the site to have a calming effect - maybe using sand and water and rocks. I am attaching files with my company logo. I would also like my name incorporated into the header - Rosalind Vantreece, LCSW, Registered Play Therapist. I've also uploaded a picture of myself for my About Page.

I like the design of these 2 website and want something similar:
www.drmaribelostrand.com
www.harrowgate-lisk.com

I would like a home page that highlights a calming graphic across the entire top of the page as well as my practice logo and my name.

I'd like a link to social media sites on the top of the homepage - facebook, pinterest.

I want a simple bar across the top with the following tabs:
Home
About Me (subtabs Who I Am, Specialties and Approach)
Counseling Services (subtabs Individual Counseling, Play Therapy, Sandplay Therapy,)
Fees
FAQs
Contact Me (would love this to be a fill in the blank contact form that sends info to my email address - should include name, phone number, email and a comment box for more information requested)
Blog (this will link with another wordpress blog)

Target Market(s)

Parents of children under age 12 with behavioral problems or are dealing with the breakup of their family through divorce - looking for someone to work with their young child. I also work with Adults that are overwhelmed and worried - often women that have many life stressors and are feeling burnt out on life and meeting everyone's needs. Families going through some type of trauma, including divorce or grief work. I also work with individuals going through a transition of religious beliefs - often exiting the religion of their youth and undergoing a crisis of faith at midlife.

Industry/Entity Type

Mental Health

Contact Information for Business Card

Rosalind Vantreece, LCSW
Registered Play Therapist
4815 Bellhaven Court
Idaho Falls, Idaho 83404
(208)555-7162
www.stillbrookwellness.com

On the opposite side, I'd like an appointment reminder area - with the following text:

Your next appointment is
_____/______/______ at ______am/pm
Please give 24 hrs notice if you need to cancel your appointment.

Coding

Coded - Design and coding required

Number of Pages Required

5+ page

Font styles to use
Sans Serif

Colors
33a6d7
9bcb3c
0355a3

Requirements
Must have
• I'd like it to be a wordpress site. I'm such a newby at web design - but I need to be able to add content and manage the site myself once it is up and running.
Nice to have
• I like the design of these 2 websites and want something similar:
• www.drmaribelostrand.com
• www.harrowgate-lisk.com
• They are clean, easy to navigate and calming.
Should not have
• Should not look like a childcare website.

```html
<!DOCTYPE html>
<html lang="en">
<head>
<meta charset="utf-8">
<title>Stillbrook Wellness – Rosalind Vantreece, LCSW</title>
<link href="https://fonts.googleapis.com/css2?family=Open+Sans:ital,wght@0,400;0,600;0,700;1,400&family=Great+Vibes&display=swap" rel="stylesheet">
<style>
:root{
  --sky:#33a6d7;
  --leaf:#9bcb3c;
  --navy:#0355a3;
  --ink:#555b61;
  --heading:#1c4f8a;
  --rule:#dcdfe3;
  --paper:#ffffff;
  --mist:#eef1f3;
}
*{margin:0;padding:0;box-sizing:border-box}
html,body{width:746px;height:1200px;overflow:hidden}
body{position:relative;font-family:"Open Sans",Arial,sans-serif;color:var(--ink);
  background:linear-gradient(#fff 0,#fff 900px,#ececec 1200px)}
.abs{position:absolute}

/* hero */
.hero{left:0;top:0;width:746px;height:357px;overflow:hidden;background:var(--mist)}
.hero-photo{left:0;top:0;width:746px;height:310px;
  background:radial-gradient(ellipse 180px 240px at 600px 170px,#b9ad9c 0,#8f8576 45%,rgba(40,90,110,0) 75%),
  linear-gradient(160deg,#2f6f86 0%,#1f5670 40%,#4a8ea3 70%,#8cb9c6 100%)}
.hero-title{left:100px;top:30px;color:#fff;font-weight:700;font-size:17.5px;letter-spacing:.6px}
.hero-script{left:98px;top:52px;color:#fff;font-family:"Great Vibes",cursive;font-size:28px}
.social{top:46px;width:27px;height:27px;border:1.6px solid #fff;border-radius:50%;display:flex;align-items:center;justify-content:center}
.dots{left:604px;top:278px;display:flex;gap:4px}
.dots span{width:7px;height:7px;border-radius:50%;background:#fff}
.dots span.on{background:var(--leaf)}
.hero-edge{left:0;top:230px}

/* header */
.brand{left:96px;top:278px;width:130px;text-align:center}
.brand-mark{width:26px;height:26px;border-radius:50%;background:var(--navy);margin:0 auto 8px}
.brand-name{font-size:11px;letter-spacing:2.6px;color:#6d7379;font-weight:400}
.brand-sub{font-size:6px;letter-spacing:2.4px;color:#6d7379;margin-top:2px}
.nav{top:332px;left:256px;display:flex;align-items:center;font-size:7px;color:#444;text-transform:uppercase}
.nav a{color:#444;text-decoration:none;margin-right:28px;padding:4px 0}
.nav a.current{background:var(--navy);color:#fff;border-radius:9px;padding:4px 12px;margin-right:19px}

/* about */
.portrait{left:100px;top:380px;width:178px;height:147px;border:1px solid #ddd;padding:3px;background:#fff}
.portrait div{width:100%;height:100%;background:linear-gradient(135deg,#d8b874,#a68a52 60%,#6b6b4a)}
.about{left:293px;top:378px;width:354px}
.about h1{font-weight:400;font-size:11.5px;color:var(--sky);margin-bottom:7px}
.about p{font-size:6.3px;line-height:11.2px;text-align:justify;margin-bottom:6px}
.btn-fill{display:inline-block;background:var(--sky);color:#fff;font-size:6.4px;font-weight:600;padding:5px 8px;border-radius:10px;margin-top:4px}

/* feature boxes */
.feature{top:552px;width:174px;height:182px;color:#fff;text-align:center;box-shadow:0 8px 10px -6px rgba(0,0,0,.15)}
.feature .ring{width:64px;height:64px;border:1.6px solid #fff;border-radius:50%;margin:17px auto 16px;display:flex;align-items:center;justify-content:center}
.feature h2{font-size:8.6px;font-weight:600;letter-spacing:.5px;margin-bottom:7px}
.feature p{font-size:7px;font-style:italic;line-height:12.8px;padding:0 26px;opacity:.92}
.btn-line{display:inline-block;border:1.4px solid #fff;border-radius:11px;font-size:6.3px;font-weight:600;padding:5px 9px;margin-top:12px}
.is-sky{left:100px;background:var(--sky)}
.is-leaf{left:286px;background:var(--leaf)}
.is-navy{left:473px;background:var(--navy)}

/* divider */
.rule{left:100px;width:546px;height:3px;border-top:1px solid var(--rule);border-bottom:1px solid var(--rule)}
.divider-badge{left:354px;top:758px;width:38px;height:38px;border-radius:50%;background:#fff;border:1px solid var(--rule)}

.section-title{left:0;width:746px;top:813px;text-align:center;color:var(--sky);font-weight:700;font-size:13px;letter-spacing:.4px}

/* posts */
.post{top:850px;width:174px}
.post .thumb{height:96px;border:1px solid #ddd;padding:2px;background:#fff}
.post .thumb div{width:100%;height:100%}
.post h3{font-size:8px;font-weight:600;color:var(--heading);line-height:14.4px;margin-top:8px;padding-right:8px;text-transform:uppercase}
.post p{font-size:6.2px;line-height:12px;margin-top:6px}
.post .meta{font-size:6.8px;color:var(--sky);margin-top:6px;display:flex;align-items:center;gap:3px}

/* footer */
.footer-badge{left:333px;top:1068px;width:70px;height:70px;border-radius:50%;background:#fff;border:1px solid var(--rule);display:flex;flex-direction:column;align-items:center;justify-content:center;color:#777;font-size:5.6px;letter-spacing:1.2px;text-align:center;line-height:8px}
.footer-nav{left:0;width:746px;top:1152px;text-align:center;font-size:6.6px;font-weight:600;color:var(--navy)}
.footer-nav span{color:var(--navy);margin:0 4px}
.copyright{left:0;width:746px;top:1169px;text-align:center;font-size:6.6px;color:#555}
</style>
</head>
<body>

<section class="abs hero">
  <div class="abs hero-photo" role="img" aria-label="Calm lake with a stack of smooth balanced stones on the shore"></div>
  <div class="abs hero-title">ROSALIND VANTREECE, LCSW,</div>
  <div class="abs hero-script">Registered Play Therapist</div>
  <a class="abs social" style="left:553px" aria-label="Social profile link"></a>
  <a class="abs social" style="left:586px" aria-label="Second social profile link"></a>
  <a class="abs social" style="left:619px" aria-label="Send an email">
    <svg width="11" height="8" viewBox="0 0 11 8"><rect width="11" height="8" rx="1" fill="#fff"/><path d="M0.5 0.8 5.5 4.6 10.5 0.8" stroke="#1f5670" stroke-width="1" fill="none"/></svg>
  </a>
  <svg class="abs hero-edge" width="746" height="130" viewBox="0 0 746 130" aria-hidden="true">
    <path d="M0 40 C160 14 310 24 420 62 C540 104 650 96 746 52 L746 130 L0 130 Z" fill="var(--mist)"/>
    <path d="M0 40 C160 14 310 24 420 62 C540 104 650 96 746 52" fill="none" stroke="#ffffff" stroke-width="2"/>
  </svg>
  <div class="abs dots"><span></span><span class="on"></span><span></span><span></span></div>
</section>

<header>
  <div class="abs brand">
    <div class="brand-mark"></div>
    <div class="brand-name">STILLBROOK</div>
    <div class="brand-sub">WELLNESS</div>
  </div>
  <nav class="abs nav">
    <a class="current">Home</a><a>About Me</a><a>Counseling Services</a><a>Fees</a><a>FAQs</a><a>Contact</a><a>Blog</a>
  </nav>
</header>

<main>
  <div class="abs portrait"><div role="img" aria-label="Portrait photo of Rosalind Vantreece"></div></div>
  <article class="abs about">
    <h1>Rosalind Vantreece, LCSW, Registered Play Therapist</h1>
    <p>Sed ut perspiciatis unde omnis iste natus error sit voluptatem accusantium doloremque laudantium, totam rem aperiam, eaque ipsa quae ab illo inventore veritatis et quasi architecto beatae vitae dicta sunt explicabo. Nemo enim ipsam voluptatem quia voluptas sit aspernatur aut odit aut fugit, sed quia consequuntur magni dolores eos qui ratione voluptatem sequi nesciunt. Neque porro quisquam est, qui dolorem ipsum quia dolor sit amet, consectetur, adipisci velit, sed quia non numquam eius modi tempora incidun.</p>
    <p>Slabore et dolore magnam aliquam quaerat voluptatem. Ut enim ad minima veniam, quis nostrum exercitationem ullam corporis suscipit laboriosam, nisi ut aliquid ex ea commodi eaque ipsa quae ab illo inventore veritatis et quasi architecto beatae vitae dicta sunt explicabomo enim ipsam voluptatem quia.</p>
    <span class="btn-fill">READ MORE »</span>
  </article>

  <div class="abs feature is-sky">
    <div class="ring"><svg width="24" height="24" viewBox="0 0 24 24" fill="none" stroke="#fff" stroke-width="1.6"><rect x="2" y="4" width="20" height="18" rx="1.5"/><path d="M2 9h20M7 1.5v5M17 1.5v5"/></svg></div>
    <h2>SCHEDULE APPOINTMENT</h2>
    <p>Start your new path in life and be the change today!</p>
    <span class="btn-line">READ MORE »</span>
  </div>
  <div class="abs feature is-leaf">
    <div class="ring"><svg width="24" height="24" viewBox="0 0 24 24" fill="none" stroke="#fff" stroke-width="2.2"><rect x="2" y="3" width="9" height="7" rx="3.5" transform="rotate(45 6.5 6.5)"/><rect x="13" y="14" width="9" height="7" rx="3.5" transform="rotate(45 17.5 17.5)"/><path d="M9 9l6 6"/></svg></div>
    <h2>LINKS &amp; RESOURCES</h2>
    <p>View recommended websites and other valuable resources.</p>
    <span class="btn-line">READ MORE »</span>
  </div>
  <div class="abs feature is-navy">
    <div class="ring"><svg width="24" height="24" viewBox="0 0 24 24" fill="none" stroke="#fff" stroke-width="1.6"><rect x="3" y="2" width="16" height="20" rx="1"/><path d="M7 8h8M7 12h6M7 16h4M14 17l7-8 2 2-7 8-3 1z"/></svg></div>
    <h2>HELPFUL FORMS</h2>
    <p>Click here to view and print forms for your appointment.</p>
    <span class="btn-line">READ MORE »</span>
  </div>

  <div class="abs rule" style="top:776px"></div>
  <div class="abs divider-badge"></div>
  <h2 class="abs section-title">RECENT BLOG POSTS</h2>

  <article class="abs post" style="left:100px">
    <div class="thumb"><div role="img" aria-label="Woman in a blue dress relaxing on a couch during a session" style="background:linear-gradient(120deg,#7a5a44,#3f8fc4 50%,#cfc3b8)"></div></div>
    <h3>Why is it so darn hard to keep new year's resolutions?</h3>
    <p>Sed ut perspiciatis unde omnis iste natus error sit volu ptatem accusantium doloremque laudantium, totamre m aperiam, eaque ipsa quae ab illo inventore.</p>
    <div class="meta"><svg width="7" height="7" viewBox="0 0 10 10" fill="none" stroke="#33a6d7" stroke-width="1.3"><rect x="1" y="2" width="8" height="7"/><path d="M1 4.5h8"/></svg>Feb 18, 2016 &nbsp;<svg width="8" height="7" viewBox="0 0 10 9"><ellipse cx="5" cy="4" rx="5" ry="3.6" fill="#33a6d7"/></svg>Comments</div>
  </article>
  <article class="abs post" style="left:286px">
    <div class="thumb"><div role="img" aria-label="Dark smooth stones resting in shallow water" style="background:linear-gradient(135deg,#d9d9d9,#4a4a4a 45%,#1d1d1d 70%,#bdbdbd)"></div></div>
    <h3>Um... little words can signal big<br>lies... you know</h3>
    <p>Sed ut perspiciatis unde omnis iste natus error sit volu ptatem accusantium doloremque laudantium, totamre m aperiam, eaque ipsa quae ab illo inventore.</p>
    <div class="meta"><svg width="7" height="7" viewBox="0 0 10 10" fill="none" stroke="#33a6d7" stroke-width="1.3"><rect x="1" y="2" width="8" height="7"/><path d="M1 4.5h8"/></svg>Feb 18, 2016 &nbsp;<svg width="8" height="7" viewBox="0 0 10 9"><ellipse cx="5" cy="4" rx="5" ry="3.6" fill="#33a6d7"/></svg>Comments</div>
  </article>
  <article class="abs post" style="left:473px">
    <div class="thumb"><div role="img" aria-label="Woman resting on green grass among daisies" style="background:linear-gradient(120deg,#4f8a2a,#8fbf4a 45%,#e9e2cf 65%,#5d9a30)"></div></div>
    <h3>Why is it so darn hard to keep new year's resolutions?</h3>
    <p>Sed ut perspiciatis unde omnis iste natus error sit volu ptatem accusantium doloremque laudantium, totamre m aperiam, eaque ipsa quae ab illo inventore.</p>
    <div class="meta"><svg width="7" height="7" viewBox="0 0 10 10" fill="none" stroke="#33a6d7" stroke-width="1.3"><rect x="1" y="2" width="8" height="7"/><path d="M1 4.5h8"/></svg>Feb 18, 2016 &nbsp;<svg width="8" height="7" viewBox="0 0 10 9"><ellipse cx="5" cy="4" rx="5" ry="3.6" fill="#33a6d7"/></svg>Comments</div>
  </article>
</main>

<footer>
  <div class="abs rule" style="top:1100px"></div>
  <div class="abs footer-badge">STILLBROOK<br>WELLNESS</div>
  <div class="abs footer-nav">HOME <span>|</span> ABOUT ME <span>|</span> COUNSELING SERVICES <span>|</span> FEES <span>|</span> FAQS <span>|</span> CONTACT <span>|</span> BLOG</div>
  <div class="abs copyright">© 2016 stillbrookwellness.com. All copycopyrights are Reserved. Privacy Policy, Terms and Conditions</div>
</footer>

</body>
</html>
```